Natural Organic Cosmetics needs a packaging design

I need package design designs for an organic, natural, unrefined shea butter packaged in a pouch like the example below. The package design should express pure, organic, freshness, moisturizing and healthy. The package design should also reflect the benefits of the product listed below. The product will be called “ORGANIC SHEA BUTTER”
MEANING OF NAME: ZENO AFRICA" meaning to Come to Africa for your natural cosmetics
Logo Text/Brand Name:
“ZENO”
Logo Styles of Interest:
Elegance
Natural
Organic
Freshness
Unrefined
From a tree nut
Target Market:
General public
Must have:
KISS : Keep it simple stupid
Note: I have a shea nuts stock photo i can provide.
Dimension:W = 7.48 InchesH = 10.43 inches Added Thursday, January 14, 2016
Industry/Entity Type
Cosmetics

```html
<!DOCTYPE html>
<html lang="en">
<head>
<meta charset="utf-8">
<title>ZENO Shea Butter – Pouch Front</title>
<link rel="stylesheet" href="https://fonts.googleapis.com/css2?family=Archivo+Black&family=Open+Sans:wght@600;700;800&display=swap">
<style>
  :root {
    --page-bg: #f4f4f4;
    --pouch-light: #fbfbfb;
    --pouch-mid: #e9e9e9;
    --brand-brown: #8c6240;
    --shea-tan: #a9815a;
    --band-brown: #8a6545;
    --ring-brown: #7a5434;
    --rule-dark: #2a2a2a;
    --tagline-grey: #333333;
    --footer-tan: #9a6d3f;
    --nut-dark: #3a2115;
    --nut-mid: #6b3a22;
    --bowl-wood: #b78652;
  }
  * { margin: 0; padding: 0; box-sizing: border-box; }
  html, body {
    width: 1200px; height: 1000px; overflow: hidden;
    background: var(--page-bg);
  }
  .canvas { position: relative; width: 1200px; height: 1000px; }

  .pouch-front {
    position: absolute; left: 340px; top: 50px;
    width: 520px; height: 900px;
    background: linear-gradient(100deg, var(--pouch-mid) 0%, var(--pouch-light) 35%, var(--pouch-light) 65%, var(--pouch-mid) 100%);
    border-radius: 6px;
    box-shadow: 0 0 0 1px #dcdcdc;
    overflow: hidden;
  }
  .zip-track {
    position: absolute; left: 0; width: 100%; height: 2px;
    background: #d9d9d9;
  }
  .zip-track.upper { top: 66px; }
  .zip-track.lower { top: 146px; }

  .brand-name {
    position: absolute; top: 168px; left: 0; width: 100%;
    text-align: center;
    font-family: "Archivo Black", sans-serif;
    font-size: 138px; line-height: 1; letter-spacing: 4px;
    color: var(--brand-brown);
  }
  .brand-rule {
    position: absolute; top: 310px; left: 70px; width: 380px; height: 3px;
    background: var(--rule-dark);
  }
  .product-name {
    position: absolute; top: 318px; left: 0; width: 100%;
    text-align: center;
    font-family: "Open Sans", sans-serif; font-weight: 800;
    font-size: 47px; letter-spacing: 4px;
    color: var(--shea-tan);
  }
  .tagline {
    position: absolute; top: 378px; left: 0; width: 100%;
    text-align: center;
    font-family: "Open Sans", sans-serif; font-weight: 700;
    font-size: 20px; letter-spacing: 1px;
    color: var(--tagline-grey);
  }
  .accent-band {
    position: absolute; top: 575px; left: 0; width: 100%; height: 99px;
    background: var(--band-brown);
  }
  .nut-window {
    position: absolute; left: 80px; top: 434px;
    width: 360px; height: 360px;
  }
  .net-weight, .usage-note {
    position: absolute; left: 0; width: 100%;
    text-align: center;
    font-family: "Open Sans", sans-serif; font-weight: 700;
    color: var(--footer-tan);
  }
  .net-weight { top: 832px; font-size: 19px; }
  .usage-note { top: 856px; font-size: 19px; }
</style>
</head>
<body>
<div class="canvas">
  <section class="pouch-front">
    <div class="zip-track upper"></div>
    <div class="zip-track lower"></div>

    <h1 class="brand-name">ZENO</h1>
    <div class="brand-rule"></div>
    <h2 class="product-name">SHEA BUTTER</h2>
    <p class="tagline">Organic • Unrefined • Natural</p>

    <div class="accent-band"></div>
    <svg class="nut-window" viewBox="0 0 360 360" role="img" aria-label="Photo of shea nuts in a wooden bowl">
      <defs>
        <radialGradient id="nutTones" cx="50%" cy="45%" r="60%">
          <stop offset="0%" stop-color="var(--nut-mid)"/>
          <stop offset="70%" stop-color="var(--nut-dark)"/>
          <stop offset="100%" stop-color="var(--bowl-wood)"/>
        </radialGradient>
      </defs>
      <ellipse cx="180" cy="180" rx="174" ry="172" transform="rotate(-12 180 180)" fill="var(--ring-brown)"/>
      <ellipse cx="180" cy="180" rx="166" ry="164" transform="rotate(-12 180 180)" fill="url(#nutTones)"/>
    </svg>

    <p class="net-weight">16 OZ.</p>
    <p class="usage-note">External Use Only</p>
  </section>
</div>
</body>
</html>
```